Webdesign für Baucoaching-Unternehmen
Ist sehr offen und ehrlich und steht zu seinen Design‘s. Mit Ihm könnt Ihr gut zusammen arbeiten und erhalten die Visualisierung gleich als Vorschlag. ... er hat kurzerhand eine eine Seite erstellt.
Zielgruppe
Die PRT Design bietet Baucoaching an.
Unsere Zielgruppe sind Privatkunden die Planen eine Immobilie zu erwerben.
Was machen wir:
Wie im Coaching üblich starten wir mit einer ist Analyse. wie wohnen Sie zur Zeit
Gehen dann weiter in die Planung. Was darf sich in Zukunft ändern.
In den nächsten Schritten Formulieren wir die Zukunft weiter aus und ergänzen diese Mit Zahlen. Die erste Kalkulation wird erstellt.
So geht es weiter bis zum Baubeginn.
Wenn gewünscht prüfen wir während der Bauphase ob alle Punkte aus der Vorbesprechung eingehalten werden.
Abschluss unserer Arbeit ist der der Einzug.
Aufgabenstellung
Es gibt schon eine Visitenkarte und ich habe mir schon mal grundsätzlich Gedanken zum Aufbau gemacht.
Das Logo und die Visitenkarte wurden auch auf Entwurfsbörse erstellt. Leider komme ich nicht an die Daten ran. Hat einer von euch eine Idee ? Danke Jonas Brulin

```html
<!DOCTYPE html>
<html lang="de">
<head>
<meta charset="utf-8">
<title>PRT Design – Baucoaching</title>
<link rel="stylesheet" href="https://fonts.googleapis.com/css2?family=Roboto:wght@300;400;500&family=Ubuntu:ital,wght@0,300;0,400;0,500;1,500&display=swap">
<style>
:root{
  --green:#38a83c;
  --text:#444;
  --text-soft:#666;
  --line:#e3e3e3;
  --dark:#252525;
}
*{box-sizing:border-box;margin:0;padding:0}
html,body{width:1200px;height:2786px;overflow:hidden}
body{position:relative;background:#fff;font-family:"Roboto",sans-serif;color:var(--text)}
.abs{position:absolute}
.heading{font-family:"Ubuntu",sans-serif;font-weight:400;color:#555}

/* nav */
.nav{left:0;top:0;width:1200px;height:44px;background:#fff;box-shadow:0 1px 4px rgba(0,0,0,.12);z-index:5}
.brand{left:20px;top:12px;display:flex;align-items:center;gap:6px;font-weight:500;font-size:13px;color:#555}
.brand-dot{width:20px;height:20px;border-radius:50%;background:var(--green)}
.nav-link{top:16px;font-size:10.5px;color:#555}
.nav-link.active{color:#333}
.nav-link.active::after{content:"";position:absolute;left:0;right:0;top:20px;height:1px;background:#333}
.search{left:1162px;top:16px}

/* hero */
.hero-photo{left:378px;top:44px;width:720px;height:330px;
  background:
    radial-gradient(ellipse 180px 150px at 430px 200px,rgba(245,214,190,.85),transparent 70%),
    radial-gradient(ellipse 160px 120px at 620px 150px,rgba(230,200,175,.7),transparent 70%),
    linear-gradient(100deg,#e6e2dc 0%,#d8d2ca 25%,#b89c82 45%,#8b6a50 60%,#c8b7a4 78%,#e8e4de 100%),
    linear-gradient(180deg,transparent 60%,rgba(110,110,115,.35) 100%)}
.hero-box{left:243px;top:104px;width:357px;height:232px;background:rgba(236,236,236,.93);padding:18px 19px}
.hero-kicker{font-size:14px;color:var(--green);margin-bottom:8px}
.hero-title{font-size:26px;line-height:32px}
.hero-title em{font-style:italic;font-weight:500}
.hero-band{left:0;top:330px}

/* cards */
.card{width:187px;height:141px;background:#fff;box-shadow:0 0 4px rgba(0,0,0,.25);text-align:center;overflow:hidden;padding-top:2px}
.card.tall{height:158px}
.card-icon{display:block;margin:0 auto}
.card-title{font-family:"Ubuntu",sans-serif;font-size:14.5px;font-weight:400;color:#444;margin-top:6px}
.card-text{font-size:11.5px;line-height:17.5px;color:var(--text-soft);margin:14px 6px 0}

/* coaching */
.phone{left:290px;top:600px;width:250px;height:345px;
  background:
    radial-gradient(ellipse 70px 130px at 95px 160px,rgba(168,104,80,.9),transparent 75%),
    radial-gradient(ellipse 120px 80px at 150px 320px,rgba(226,190,165,.9),transparent 75%),
    linear-gradient(180deg,#fff 0%,#f5f3f1 100%)}
.phone-body{left:318px;top:604px;width:145px;height:290px;border-radius:20px;background:linear-gradient(180deg,#3c3c3c 0%,#4a4a4a 20%,#9a6a55 40%,#b4826a 65%,#7a6a5e 100%)}
.coach-kicker{left:631px;top:606px;font-size:14px;color:var(--green)}
.coach-title{left:631px;top:630px;font-size:26px;line-height:32px}
.coach-title em{font-weight:500}
.coach-line{left:631px;font-family:"Ubuntu",sans-serif;font-size:14px;color:#555}

.divider{left:0;width:1200px;height:2px;background:#eee;box-shadow:0 1px 2px rgba(0,0,0,.12)}

/* target list */
.section-title{left:0;width:1200px;text-align:center;font-size:24px}
.list{top:1035px;width:344px}
.list li{list-style:none;height:34.4px;border-bottom:1px solid var(--line);font-size:14px;color:#444;padding:9px 0 0 10px;display:flex;gap:10px;align-items:flex-start}
.list li::before{content:"";margin-top:4px;border-left:5px solid #444;border-top:4px solid transparent;border-bottom:4px solid transparent}

/* tabs */
.tabs{left:250px;top:1357px;display:flex}
.tab{height:40px;padding:11px 16px;font-size:14px;color:#444}
.tab.active{color:var(--green);border:1px solid var(--line);border-bottom:1px solid #fff;background:#fff;position:relative;z-index:2}
.panel{left:250px;top:1396px;width:700px;height:503px;border:1px solid var(--line)}
.panel-text{left:276px;top:1422px;width:318px;font-family:"Ubuntu",sans-serif;font-size:14px;line-height:20.6px;color:#444}
.video{left:605px;top:1422px;width:320px;height:180px;
  background:
    linear-gradient(90deg,transparent 49.5%,rgba(255,255,255,.5) 49.5%,rgba(255,255,255,.5) 50%,transparent 50%),
    radial-gradient(ellipse 60px 40px at 80px 50px,rgba(200,230,215,.8),transparent 75%),
    radial-gradient(ellipse 70px 60px at 250px 100px,rgba(150,110,80,.6),transparent 75%),
    linear-gradient(180deg,#d8d6d0 0%,#b8b4ac 45%,#8f887e 70%,#6e6a64 100%)}
.video-bar{left:605px;top:1422px;width:320px;height:34px;background:linear-gradient(180deg,rgba(0,0,0,.55),transparent);display:flex;align-items:center;gap:8px;padding:0 8px;color:#fff;font-size:11.5px}
.video-bar i{width:22px;height:22px;border-radius:50%;background:#fff}
.play{left:745px;top:1499px;width:42px;height:28px;border-radius:7px;background:#222}
.site-photo{left:605px;top:1613px;width:320px;height:213px;
  background:
    radial-gradient(ellipse 40px 90px at 70px 130px,rgba(200,210,60,.75),transparent 75%),
    radial-gradient(ellipse 40px 80px at 140px 140px,rgba(205,215,70,.7),transparent 75%),
    linear-gradient(180deg,#b9c4c9 0%,#9aa1a2 35%,#d6d7d2 65%,#bfc0bb 100%)}

/* steps */
.advisor{left:269px;top:1989px;width:311px;height:206px;
  background:
    radial-gradient(ellipse 60px 80px at 130px 80px,rgba(190,160,140,.85),transparent 75%),
    radial-gradient(ellipse 80px 90px at 150px 170px,rgba(120,90,65,.8),transparent 75%),
    linear-gradient(110deg,#5f7040 0%,#b7b39f 30%,#e8e5dd 55%,#3d3d3b 75%,#d8d6d0 100%)}
.steps{left:606px;top:2004px;width:338px}
.step-row{display:flex;align-items:center;gap:8px;font-size:8px;color:#aaa;line-height:9px}
.step-row span{text-align:center}
.step-row .now{color:var(--green)}
.step-row i{flex:1;height:1px;background:#ccc}
.question{left:606px;top:2040px;font-family:"Ubuntu",sans-serif;font-size:12px;color:#777}
.option{left:606px;font-family:"Ubuntu",sans-serif;font-size:13.5px;color:#666;display:flex;align-items:center;gap:4px}
.option::before{content:"";width:8px;height:8px;border:1px solid #888;border-radius:50%}
.next{left:606px;top:2153px;width:338px;height:24px;background:var(--green);color:#fff;font-size:13px;font-weight:500;text-align:center;line-height:24px}
.benefits{left:0;top:2220px;width:1200px;display:flex;justify-content:center;font-family:"Ubuntu",sans-serif;font-size:14px;color:#555}
.benefit{display:flex;align-items:center;gap:8px;padding:0 15px;border-right:1px solid var(--line)}
.benefit:last-child{border-right:0}

/* to-top */
.to-top{left:1147px;width:40px;height:40px;border-radius:50%;background:#777;z-index:6}
.to-top.light{background:#ddd}
.to-top svg{display:block;margin:12px auto 0}

/* footer */
.footer{left:0;top:2506px;width:1200px;height:280px;background:var(--dark)}
.f-brand{left:20px;top:2540px;display:flex;align-items:center;gap:6px;font-weight:500;font-size:14px;color:#fff}
.f-brand .brand-dot{background:#fff}
.f-about{left:18px;top:2599px;width:260px;font-size:14px;line-height:21px;color:#fff}
.social{top:2661px;width:14px;height:14px;border-radius:50%;background:#fff}
.f-title{top:2530px;font-family:"Ubuntu",sans-serif;font-size:18px;font-weight:500;color:#fff}
.f-text{left:318px;font-size:11.5px;color:#fff}
.f-link{left:675px;font-size:14px;color:#aaa}
.field{left:919px;width:262px;height:30px;border-bottom:1px solid #555;font-size:9px;color:#ddd;padding:10px 0 0 14px}
.subscribe{left:919px;top:2609px;width:262px;height:25px;border:1px solid #ddd;color:#fff;font-size:13px;text-align:center;line-height:23px}
.f-rule{left:262px;top:2748px;width:675px;height:1px;background:#444}
.f-copy{left:262px;top:2775px;font-size:8px;color:#999}
.f-legal{left:772px;top:2775px;font-size:8px;color:#999;display:flex;gap:11px}
</style>
</head>
<body>

<header class="abs nav">
  <div class="abs brand"><span class="brand-dot"></span>PRT DESIGN</div>
  <span class="abs nav-link active" style="left:328px">Home</span>
  <span class="abs nav-link" style="left:385px">geniale Idee</span>
  <span class="abs nav-link" style="left:471px">smart-dream-bau</span>
  <span class="abs nav-link" style="left:580px">handwerk wird digital</span>
  <span class="abs nav-link" style="left:709px">prt design</span>
  <svg class="abs search" width="10" height="10" viewBox="0 0 10 10"><circle cx="4" cy="4" r="3" fill="none" stroke="#444" stroke-width="1.5"/><line x1="6.2" y1="6.2" x2="9" y2="9" stroke="#444" stroke-width="1.6"/></svg>
</header>

<section>
  <div class="abs hero-photo" role="img" aria-label="Familie sitzt lachend unter einem Kartondach im Wohnzimmer"></div>
  <div class="abs hero-box">
    <p class="hero-kicker">Ihre Idee | unser know how | eine perfekte Lösung</p>
    <h1 class="heading hero-title">Wir greifen Ihren Gedanke des Umbaus, Neubaus oder der Sanierung auf und Modelieren<br><em>Ihr Gefühl des Einzugs!</em></h1>
  </div>
  <svg class="abs hero-band" width="1200" height="52" viewBox="0 0 1200 52"><polygon points="378,46 1200,12 1200,0 1098,0 1098,14" fill="#fff"/><polygon points="0,46 1200,20 1200,52 0,52" fill="var(--green)"/></svg>
</section>

<section>
  <div class="abs card" style="left:275px;top:424px">
    <svg class="card-icon" role="img" aria-label="Symbol Kommunikation" width="46" height="46" viewBox="0 0 46 46"><rect x="4" y="4" width="18" height="12" rx="2" fill="none" stroke="var(--green)" stroke-width="1.6"/><rect x="26" y="8" width="16" height="10" rx="2" fill="none" stroke="var(--green)" stroke-width="1.6"/><circle cx="23" cy="28" r="6" fill="none" stroke="var(--green)" stroke-width="1.6"/><path d="M11 44c2-7 7-9 12-9s10 2 12 9" fill="none" stroke="var(--green)" stroke-width="1.6"/></svg>
    <h3 class="card-title">Kommunikation</h3>
    <p class="card-text">Lorem ipsum dolor sit amet, consectetur adipiscing elit. Ut elit tellus, luctus nec ullamcorper</p>
  </div>
  <div class="abs card" style="left:512px;top:424px">
    <svg class="card-icon" role="img" aria-label="Symbol Datenschutz" width="50" height="48" viewBox="0 0 50 48"><path d="M4 30l10-10 8 4 6-4 8 2 10 8-10 10-8-6-6 4-8-4z" fill="none" stroke="var(--green)" stroke-width="1.6"/><path d="M25 4v6M14 8l3 5M36 8l-3 5" stroke="var(--green)" stroke-width="1.6"/></svg>
    <h3 class="card-title">Datenschutz</h3>
    <p class="card-text">Lorem ipsum dolor sit amet, consectetur adipiscing elit. Ut elit tellus, luctus nec ullamcorper</p>
  </div>
  <div class="abs card" style="left:750px;top:424px">
    <svg class="card-icon" role="img" aria-label="Symbol Zahnrad und Glühbirne" width="48" height="48" viewBox="0 0 48 48"><circle cx="32" cy="16" r="10" fill="none" stroke="var(--green)" stroke-width="1.6"/><path d="M28 26v8h8v-8" fill="none" stroke="var(--green)" stroke-width="1.6"/><circle cx="13" cy="32" r="7" fill="none" stroke="var(--green)" stroke-width="1.6"/><circle cx="13" cy="32" r="2.5" fill="var(--green)"/></svg>
    <h3 class="card-title">Platzhalter</h3>
    <p class="card-text">Lorem ipsum dolor sit amet, consectetur adipiscing elit. Ut elit tellus, luctus nec ullamcorper</p>
  </div>
</section>

<section>
  <div class="abs phone" role="img" aria-label="Hand hält ein Smartphone mit Raumvermessung einer Ziegelwand"></div>
  <div class="abs phone-body" aria-hidden="true"></div>
  <p class="abs coach-kicker">Baucoaching + SIL-System</p>
  <h2 class="abs heading coach-title">Wer nicht weiß, was er will,<br>zahlt in der Regel zu <em>viel !</em>“</h2>
  <p class="abs coach-line" style="top:721px">Wir planen mit Ihnen Ihr neues Heim.</p>
  <p class="abs coach-line" style="top:754px">Was ist Ihr Ziel?</p>
  <p class="abs coach-line" style="top:787px">Wie soll es fertig aussehen?</p>
  <p class="abs coach-line" style="top:820px">Wann wollen Sie einziehen?</p>
</section>

<div class="abs divider" style="top:962px"></div>

<section>
  <h2 class="abs heading section-title" style="top:979px">Für wen?</h2>
  <ul class="abs list" style="left:250px">
    <li>Architekten und Bauträger</li>
    <li>gemeinsam erzeugen wir das Gefühl des Einzugs</li>
    <li>Kommunikation, Dokumentation!</li>
    <li>Qualitätsnachweis 3D Dokumentation.</li>
    <li>Gewerksübergreifend aus einer cloud</li>
    <li>W-LAN Auf der Baustelle</li>
  </ul>
  <ul class="abs list" style="left:606px">
    <li>Bauherren</li>
    <li>gemeinsam erzeugen wir das Gefühl des Einzugs</li>
    <li>Kommunikation, Planung!</li>
    <li>Qualitätsnachweis 3D Dokumentation.</li>
    <li>Gewerksübergreifend aus einer cloud</li>
    <li>W-LAN Auf der Baustelle</li>
  </ul>
</section>

<div class="abs divider" style="top:1279px"></div>

<section>
  <h2 class="abs heading section-title" style="top:1300px">Einsatzgebiete</h2>
  <div class="abs panel"></div>
  <div class="abs tabs">
    <span class="tab active">Sanierung</span>
    <span class="tab">Neubau</span>
    <span class="tab">Umgestaltung</span>
  </div>
  <p class="abs panel-text">Lorem ipsum dolor sit amet, consetetur sadipscing elitr, sed diam nonumy eirmod tempor invidunt ut labore et dolore magna aliquyam erat, sed diam voluptua. At vero eos et accusam et justo duo dolores et ea rebum. Stet clita kasd gubergren, no sea takimata sanctus est Lorem ipsum dolor sit amet. Lorem ipsum dolor sit amet, consetetur sadipscing elitr, sed diam nonumy eirmod tempor invidunt ut labore et dolore magna aliquyam erat, sed diam voluptua. At vero eos et accusam et justo duo dolores et ea rebum. Stet clita kasd gubergren, no sea takimata sanctus est Lorem ipsum dolor sit amet. Lorem ipsum dolor sit amet, consetetur sadipscing elitr, sed diam nonumy eirmod tempor invidunt ut labore et dolore magna aliquyam erat, sed diam voluptua. At vero eos et accusam et justo duo dolores et ea rebum. Stet clita kasd gubergren, no sea takimata sanctus est Lorem ipsum dolor sit amet.</p>
  <div class="abs video" role="img" aria-label="Video: Raumscan-Vermessung einer Küche im Vergleich zur Handmessung"></div>
  <div class="abs video-bar"><i></i>Raumscan: Now Available On Any LiDAR-Enabled i...</div>
  <div class="abs play"><svg width="42" height="28" viewBox="0 0 42 28"><polygon points="17,8 27,14 17,20" fill="#fff"/></svg></div>
  <div class="abs site-photo" role="img" aria-label="Zwei Bauleiter mit Helm prüfen Pläne auf einer Baustelle"></div>
</section>

<div class="abs divider" style="top:1910px"></div>

<section>
  <h2 class="abs heading section-title" style="top:1933px">In 4 Schritten zum kostenlosen Angebot</h2>
  <div class="abs advisor" role="img" aria-label="Berater mit Smartphone im hellen Büro"></div>
  <div class="abs steps">
    <div class="step-row"><span class="now">aktuelle<br>Situation</span><i></i><span>Ihr<br>Vorhaben</span><i></i><span>Umfang</span><i></i><span>Kontaktdaten</span></div>
  </div>
  <p class="abs question">Wie wohnen Sie zurzeit?</p>
  <p class="abs option" style="top:2068px">Mietwohnung</p>
  <p class="abs option" style="top:2089px">Eigentumswohnung</p>
  <p class="abs option" style="top:2110px">Mietshaus</p>
  <p class="abs option" style="top:2131px">eigenes Haus</p>
  <div class="abs next">weiter</div>
  <div class="abs benefits">
    <span class="benefit"><svg width="14" height="14" viewBox="0 0 14 14"><rect x="1" y="2" width="11" height="11" fill="none" stroke="var(--green)" stroke-width="1.4"/><path d="M4 7l3 3 6-8" fill="none" stroke="var(--green)" stroke-width="1.6"/></svg>Terminverfolgung</span>
    <span class="benefit"><svg width="14" height="14" viewBox="0 0 14 14"><rect x="1" y="2" width="11" height="11" fill="none" stroke="var(--green)" stroke-width="1.4"/><path d="M4 7l3 3 6-8" fill="none" stroke="var(--green)" stroke-width="1.6"/></svg>Budget kontrolle</span>
    <span class="benefit"><svg width="14" height="14" viewBox="0 0 14 14"><rect x="1" y="2" width="11" height="11" fill="none" stroke="var(--green)" stroke-width="1.4"/><path d="M4 7l3 3 6-8" fill="none" stroke="var(--green)" stroke-width="1.6"/></svg>gesteigerte Qualität</span>
    <span class="benefit"><svg width="14" height="14" viewBox="0 0 14 14"><rect x="1" y="2" width="11" height="11" fill="none" stroke="var(--green)" stroke-width="1.4"/><path d="M4 7l3 3 6-8" fill="none" stroke="var(--green)" stroke-width="1.6"/></svg>Bauzeit geniessen</span>
  </div>
</section>

<div class="abs divider" style="top:2265px"></div>

<section>
  <div class="abs card tall" style="left:275px;top:2310px">
    <svg class="card-icon" role="img" aria-label="Symbol Buch" width="46" height="42" viewBox="0 0 46 42"><path d="M4 8h16l3 3 3-3h16v30H26l-3 2-3-2H4z" fill="var(--green)"/><path d="M23 11v28" stroke="#fff" stroke-width="1.5"/></svg>
    <h3 class="card-title">Backstory</h3>
    <p class="card-text">Lorem ipsum dolor sit amet, consectetur adipiscing elit. Ut elit tellus, luctus nec ullamcorper mattis, pulvinar dapibus leo.</p>
  </div>
  <div class="abs card tall" style="left:512px;top:2310px">
    <svg class="card-icon" role="img" aria-label="Symbol Datenschutz" width="50" height="48" viewBox="0 0 50 48"><path d="M4 30l10-10 8 4 6-4 8 2 10 8-10 10-8-6-6 4-8-4z" fill="none" stroke="var(--green)" stroke-width="1.6"/><path d="M25 4v6M14 8l3 5M36 8l-3 5" stroke="var(--green)" stroke-width="1.6"/></svg>
    <h3 class="card-title">Datenschutz</h3>
    <p class="card-text">Lorem ipsum dolor sit amet, consectetur adipiscing elit. Ut elit tellus, luctus nec ullamcorper mattis, pulvinar dapibus leo.</p>
  </div>
  <div class="abs card tall" style="left:750px;top:2310px">
    <svg class="card-icon" role="img" aria-label="Symbol Erdkugel" width="48" height="48" viewBox="0 0 48 48"><circle cx="24" cy="24" r="20" fill="none" stroke="var(--green)" stroke-width="2"/><path d="M12 14c6 2 6 8 12 8s4 8 10 10M30 8c-2 4 2 6 6 6" fill="none" stroke="var(--green)" stroke-width="2"/></svg>
    <h3 class="card-title">Zukunft Erde</h3>
    <p class="card-text">Lorem ipsum dolor sit amet, consectetur adipiscing elit. Ut elit tellus, luctus nec ullamcorper mattis, pulvinar dapibus leo.</p>
  </div>
</section>

<footer>
  <div class="abs footer"></div>
  <div class="abs f-brand"><span class="brand-dot"></span>PRT DESIGN</div>
  <p class="abs f-about">Lorem ipsum dolor sit amet, consetetur sadipscing elitr, sed diam</p>
  <span class="abs social" style="left:13px"></span>
  <span class="abs social" style="left:38px"></span>
  <span class="abs social" style="left:63px"></span>
  <span class="abs social" style="left:88px"></span>

  <h4 class="abs f-title" style="left:318px">Kontakt</h4>
  <p class="abs f-text" style="top:2568px">PRT DESIGN</p>
  <p class="abs f-text" style="top:2586px">Lindenweg 47</p>
  <p class="abs f-text" style="top:2603px">78462 Seestadt</p>
  <p class="abs f-text" style="top:2638px;left:322px">+49 7700 555 0123</p>
  <p class="abs f-text" style="top:2655px;left:322px">Jonas.Brulin@PRT-Design.de</p>

  <h4 class="abs f-title" style="left:675px">Quick Links</h4>
  <p class="abs f-link" style="top:2572px">Blog</p>
  <p class="abs f-link" style="top:2596px">Project</p>
  <p class="abs f-link" style="top:2621px">Contact us</p>
  <p class="abs f-link" style="top:2645px">Our Team</p>

  <div class="abs field" style="top:2521px">Name</div>
  <div class="abs field" style="top:2564px">Email</div>
  <div class="abs subscribe">abonnieren</div>

  <div class="abs f-rule"></div>
  <p class="abs f-copy">Copyright © 2021 RV DESIGN. All rights reserved.</p>
  <p class="abs f-legal"><span>Legal</span><span>Term of service</span><span>GDPR</span><span>Term of use</span></p>
</footer>

<div class="abs to-top light" style="top:508px"><svg width="14" height="10" viewBox="0 0 14 10"><path d="M2 8l5-5 5 5" fill="none" stroke="#fff" stroke-width="2.5"/></svg></div>
<div class="abs to-top" style="top:886px"><svg width="14" height="10" viewBox="0 0 14 10"><path d="M2 8l5-5 5 5" fill="none" stroke="#fff" stroke-width="2.5"/></svg></div>
<div class="abs to-top" style="top:1347px"><svg width="14" height="10" viewBox="0 0 14 10"><path d="M2 8l5-5 5 5" fill="none" stroke="#fff" stroke-width="2.5"/></svg></div>
<div class="abs to-top" style="top:1808px"><svg width="14" height="10" viewBox="0 0 14 10"><path d="M2 8l5-5 5 5" fill="none" stroke="#fff" stroke-width="2.5"/></svg></div>
<div class="abs to-top" style="top:2268px"><svg width="14" height="10" viewBox="0 0 14 10"><path d="M2 8l5-5 5 5" fill="none" stroke="#fff" stroke-width="2.5"/></svg></div>
<div class="abs to-top" style="top:2729px;background:#3a3a3a"><svg width="14" height="10" viewBox="0 0 14 10"><path d="M2 8l5-5 5 5" fill="none" stroke="#222" stroke-width="2.5"/></svg></div>

</body>
</html>
```